Poster for Stores

We need a poster design for my company, ourcornerville.net. The company is a social networking site oriented around the town.

I have a slogan for the site....Helping Town Connect with People.

I want the background color to be a type of green.

I want to have a picture of a generic town in the background.

I would some of the below text in the poster to be:

1) All your local town deals in one place.
2) its's free..no cost
3) create town events...create groups...blog or forum about/around the town.
4) find out about city/town services

Industry/Entity Type

Town

```html
<!DOCTYPE html>
<html lang="en">
<head>
<meta charset="utf-8">
<title>ourcornerville.net – Store Poster</title>
<link rel="stylesheet" href="https://fonts.googleapis.com/css2?family=Ubuntu:wght@400;500;700&display=swap">
<style>
  :root {
    --lime: #b8f03a;
    --lime-light: #c9f56a;
    --lime-deep: #8fcf2a;
    --green-dark: #2e8a1f;
    --green-band: #3a9426;
    --green-ink: #1f6e14;
    --white: #ffffff;
  }
  * { margin: 0; padding: 0; box-sizing: border-box; }
  html, body {
    width: 857px; height: 1200px; overflow: hidden;
    background: var(--lime);
  }
  .poster {
    position: relative;
    width: 857px; height: 1200px;
    overflow: hidden;
    background: var(--lime);
    font-family: "Ubuntu", sans-serif;
  }
  .town-scene {
    position: absolute;
    left: 0; top: 150px;
    width: 857px; height: 780px;
    background:
      linear-gradient(180deg, var(--lime-light) 0%, var(--lime) 22%, var(--lime-deep) 55%, #a3e035 78%, var(--lime) 100%);
  }
  .site-name {
    position: absolute;
    left: 36px; top: -6px;
    font-weight: 700;
    font-size: 90px;
    letter-spacing: -1px;
    color: var(--green-dark);
    white-space: nowrap;
  }
  .cursor-icon {
    position: absolute;
    left: 722px; top: 98px;
    width: 40px; height: 56px;
  }
  .slogan {
    position: absolute;
    left: 42px; top: 196px;
    font-weight: 700;
    font-size: 82px;
    line-height: 84px;
    color: var(--white);
    -webkit-text-stroke: 3px var(--green-ink);
    paint-order: stroke fill;
  }
  .feature {
    position: absolute;
    background: var(--green-band);
    color: var(--white);
    font-weight: 500;
    white-space: nowrap;
    display: flex; align-items: center; justify-content: center;
  }
  .feature--deals {
    left: 104px; top: 792px; width: 734px; height: 72px;
    font-size: 37px;
    transform: rotate(-2.2deg);
  }
  .feature--free {
    left: 441px; top: 880px; width: 350px; height: 48px;
    font-size: 35px;
  }
  .feature--community {
    left: 22px; top: 934px; width: 772px; height: 108px;
    font-size: 35px; line-height: 38px;
    white-space: normal; text-align: left;
    justify-content: flex-start; padding-left: 16px;
    transform: rotate(1.6deg);
  }
  .feature--services {
    left: 110px; top: 1056px; width: 713px; height: 58px;
    font-size: 35px;
  }
  .call-to-action {
    position: absolute;
    left: 34px; top: 1140px;
    font-size: 29px;
    font-weight: 400;
    color: var(--green-ink);
    white-space: nowrap;
  }
  .call-to-action strong { font-weight: 700; }
</style>
</head>
<body>
<main class="poster">
  <div class="town-scene" role="img" aria-label="Green-tinted photograph of a busy old town square with tall historic buildings and crowds of people"></div>

  <div class="site-name">ourcornerville.net</div>
  <svg class="cursor-icon" viewBox="0 0 40 56" aria-hidden="true">
    <path d="M4 2 L4 44 L14 34 L21 52 L28 49 L21 32 L35 32 Z" fill="#ffffff" stroke="#111" stroke-width="2.5" stroke-linejoin="round"/>
  </svg>

  <h1 class="slogan">Helping Town<br>Connect with<br>People</h1>

  <p class="feature feature--deals">All your local town deals in one place.</p>
  <p class="feature feature--free">Its's free - no cost</p>
  <p class="feature feature--community">Create town events, create groups,<br>blog or forum about/around the town.</p>
  <p class="feature feature--services">Find out about city/town services</p>

  <p class="call-to-action">visit now <strong>www.ourcornerville.net</strong> and learn more</p>
</main>
</body>
</html>
```